Business Card Design

Business card design.

Business card is to have logo, website address and email address.

Website is www.brightkettle.ie
Email is info@brightkettle.ie
Logo uploaded

I have ordered Business Card Printing via Print Harbor, the Double-sided colour printed option with gloss finish.

Industry/Entity Type

Business

```html
<!DOCTYPE html>
<html lang="en">
<head>
<meta charset="utf-8">
<title>Bright Kettle Business Card</title>
<link href="https://fonts.googleapis.com/css2?family=Ubuntu:wght@400;700&display=swap" rel="stylesheet">
<style>
  :root {
    --backdrop: #c48a57;
    --card: #ffffff;
    --ink: #111111;
    --brand-red: #d40000;
    --brand-red-dark: #8e0000;
    --swoosh: #141414;
    --card-edge: #3a2a1e;
  }
  * { margin: 0; padding: 0; box-sizing: border-box; }
  html, body {
    width: 1200px;
    height: 373px;
    overflow: hidden;
    background: var(--backdrop);
    font-family: "Ubuntu", sans-serif;
  }
  .canvas {
    position: relative;
    width: 1200px;
    height: 373px;
  }
  .card {
    position: absolute;
    top: 22px;
    width: 562px;
    height: 321px;
    background: var(--card);
    overflow: hidden;
  }
  .card--front { left: 28px; border-radius: 18px; }
  .card--back {
    left: 617px;
    width: 563px;
    border-radius: 28px;
    border: 1px solid var(--card-edge);
  }
  .brand {
    position: absolute;
    left: 0;
    right: 0;
    display: flex;
    align-items: center;
    justify-content: center;
    gap: 14px;
  }
  .card--front .brand { top: 128px; }
  .card--back .brand { top: 150px; }
  .brand__dot {
    width: 40px;
    height: 40px;
    border-radius: 50%;
    background: var(--brand-red);
    flex: none;
  }
  .brand__name {
    font-weight: 700;
    font-size: 42px;
    letter-spacing: -0.5px;
    color: var(--ink);
    line-height: 1;
  }
  .wave {
    position: absolute;
    left: 0;
    top: 0;
    width: 562px;
    height: 321px;
  }
  .contact {
    position: absolute;
    left: 34px;
    top: 288px;
    display: flex;
    align-items: center;
    gap: 8px;
    color: #ffffff;
    font-size: 17px;
  }
  .contact__icon { width: 16px; height: 13px; }
</style>
</head>
<body>
<main class="canvas">
  <section class="card card--front" aria-label="Card front">
    <svg class="wave" viewBox="0 0 562 321" aria-hidden="true">
      <defs>
        <linearGradient id="redBand" x1="0" y1="0" x2="1" y2="0">
          <stop offset="0" stop-color="var(--brand-red-dark)"/>
          <stop offset="0.6" stop-color="var(--brand-red)"/>
          <stop offset="1" stop-color="#ff1a1a"/>
        </linearGradient>
      </defs>
      <path d="M0,246 C160,236 300,262 420,292 C480,306 530,292 562,264 L562,282 C520,308 468,316 400,308 C300,288 150,262 0,264 Z" fill="var(--swoosh)"/>
      <path d="M0,266 C150,266 300,296 400,312 C470,320 530,302 562,286 L562,321 L0,321 Z" fill="url(#redBand)"/>
    </svg>
    <div class="brand">
      <span class="brand__dot"></span>
      <span class="brand__name">BRIGHTKETTLE.IE</span>
    </div>
    <p class="contact">
      <svg class="contact__icon" viewBox="0 0 16 13" aria-hidden="true">
        <rect x="0.5" y="0.5" width="15" height="12" rx="1.5" fill="#ffffff"/>
        <path d="M1,1.5 L8,7.5 L15,1.5" fill="none" stroke="var(--brand-red)" stroke-width="1.4"/>
      </svg>
      <span class="contact__email">info@brightkettle.ie</span>
    </p>
  </section>

  <section class="card card--back" aria-label="Card back">
    <div class="brand">
      <span class="brand__dot"></span>
      <span class="brand__name">BRIGHTKETTLE.IE</span>
    </div>
  </section>
</main>
</body>
</html>
```